Business Card Design Project

we need a business card design for our company: www.plomvik.ch
It's important to include our already existing logo (see website)

```html
<!DOCTYPE html>
<html lang="en">
<head>
<meta charset="utf-8">
<title>Plomvik – Business Card</title>
<link href="https://fonts.googleapis.com/css2?family=Open+Sans:wght@400;600;700&display=swap" rel="stylesheet">
<style>
  :root {
    --bg: #e9eaec;
    --blue-light: #3f86d6;
    --blue: #1d5db4;
    --blue-deep: #0c3c88;
    --tag-blue: #9cc4ef;
    --ink: #1d1d1f;
    --muted: #6d7278;
    --rule: #c9ccd1;
    --paper: #ffffff;
  }
  * { box-sizing: border-box; margin: 0; padding: 0; }
  html, body { width: 1200px; height: 944px; overflow: hidden; }
  body {
    background: var(--bg);
    font-family: "Open Sans", Arial, sans-serif;
    position: relative;
  }
  .card {
    position: absolute;
    width: 560px;
    height: 340px;
    border-radius: 22px;
    overflow: hidden;
    box-shadow: 0 10px 28px rgba(0,0,0,.22);
  }
  .brand { display: inline-block; text-align: right; }
  .brand-name { text-align: left; white-space: nowrap; }
  .brand-tagline { white-space: nowrap; }

  /* Front */
  .card-front {
    left: 60px; top: 60px;
    background: radial-gradient(ellipse at 45% 40%, var(--blue-light) 0%, var(--blue) 45%, var(--blue-deep) 100%);
  }
  .front-brand {
    position: absolute;
    left: 70px; top: 105px;
    color: var(--paper);
  }
  .front-brand .brand-name {
    font-size: 96px;
    font-weight: 700;
    letter-spacing: -2px;
    line-height: 1;
  }
  .front-brand .brand-tagline {
    margin-top: 10px;
    font-size: 19px;
    font-weight: 400;
    color: var(--tag-blue);
    letter-spacing: .5px;
  }

  /* Back */
  .card-back {
    left: 580px; top: 520px;
    background: var(--paper);
  }
  .back-brand {
    position: absolute;
    left: 34px; top: 118px;
  }
  .back-brand .brand-name {
    font-size: 58px;
    font-weight: 700;
    letter-spacing: -1px;
    color: var(--blue);
    line-height: 1;
  }
  .back-brand .brand-tagline {
    margin-top: 6px;
    font-size: 11px;
    color: var(--muted);
    letter-spacing: .3px;
  }
  .divider {
    position: absolute;
    left: 296px; top: 40px;
    width: 2px; height: 250px;
    background: var(--rule);
  }
  .edge-band {
    position: absolute;
    right: 0; top: 120px;
    width: 14px; height: 190px;
    background: var(--blue);
  }
  .contact {
    position: absolute;
    left: 318px; top: 40px;
    color: var(--ink);
  }
  .person-name { font-size: 20px; font-weight: 400; }
  .person-role { font-size: 15px; margin-top: 2px; }
  .address { margin-top: 22px; font-size: 17px; line-height: 1.3; }
  .lines { margin-top: 14px; list-style: none; font-size: 17px; line-height: 1.35; }
  .lines li { display: flex; align-items: center; gap: 8px; }
  .lines svg { width: 12px; height: 12px; flex: none; fill: var(--ink); }
</style>
</head>
<body>

<section class="card card-front" aria-label="Card front">
  <div class="brand front-brand">
    <div class="brand-name">Plomvik</div>
    <div class="brand-tagline">BUSINESS SOFTWARE STUDIO</div>
  </div>
</section>

<section class="card card-back" aria-label="Card back">
  <div class="brand back-brand">
    <div class="brand-name">Plomvik</div>
    <div class="brand-tagline">BUSINESS SOFTWARE STUDIO</div>
  </div>
  <div class="divider"></div>
  <div class="contact">
    <p class="person-name">Jonas Brandell</p>
    <p class="person-role">Manager</p>
    <p class="address">Plomvik AG<br>Lindenhofweg 12<br>8004 Zürich</p>
    <ul class="lines">
      <li><svg viewBox="0 0 12 12" aria-hidden="true"><path d="M2.5 0.8 L4.6 3.2 L3.6 4.6 Q4.6 6.9 7.4 8.4 L8.8 7.4 L11.2 9.5 L10 11.2 Q5.5 11 2.2 6.8 Q0.6 4.4 0.8 2.1 Z"/></svg>+41 44 301 17 40</li>
      <li><svg viewBox="0 0 12 12" aria-hidden="true"><rect x="0.5" y="2" width="11" height="8" rx="1"/><path d="M1 2.6 L6 6.6 L11 2.6" stroke="#fff" stroke-width="1" fill="none"/></svg>info@plomvik.ch</li>
      <li><svg viewBox="0 0 12 12" aria-hidden="true"><circle cx="6" cy="6" r="5.5"/></svg>plomvik.ch</li>
      <li><svg viewBox="0 0 12 12" aria-hidden="true"><circle cx="6" cy="6" r="5.2" fill="none" stroke="#1d1d1f" stroke-width="1.2"/><ellipse cx="6" cy="6" rx="2.2" ry="5.2" fill="none" stroke="#1d1d1f" stroke-width="1"/><path d="M0.8 6 H11.2" stroke="#1d1d1f" stroke-width="1"/></svg>www.plomvik.ch</li>
    </ul>
  </div>
  <div class="edge-band"></div>
</section>

</body>
</html>
```